Banner (html, flash, gifs, jpgs or html5) - BrightOrbits

We need horizontal banners and copy created that would get people to click for holiday purposes that will go here: https://www.brightorbits.example/blog.htm
The specs on the rich media unit ads are:
•	Audience - lifestyle interest, 18-35 age group
•	Multiple calls to action offer opportunities to further engage
•	Unit dimensions are 800x80
•	Max file size 1 MB
•	We can take html, flash, gifs, jpgs or html5
Please include a thumbnail image for 2 of the 3 options below:
1) a thumbnail image for Free Sign Up - https://www.brightorbits.example/ppcRegistration2.htm
2) a thumbnail image for Astrology Reports - astrology.brightorbits.example
3) a thumbnail image for iOS and Android app
and
Include a coupon code respective of the holiday you choose:
Promo	Day	Holiday
NewYou	1/1	New Year's Day
Dream	1/18	Martin Luther King, Jr. Day
BeMine	2/14	Valentines Day
PresDay	2/15	Presidents Day
NewLove	3/27	Spring
ForHer	5/8	Mothers Day
MDUSA	5/30	Memorial Day
ForHim	6/19	Fathers day
Fireworks	7/4	Independence Day
Passion	8/1	Summer Love
Fall4U	10/10	Columbus Day
Treat	10/31	Halloween
ThankYou	11/24	Thanksgiving Day
Snuggle	12/25	Happy Holidays
Bright Orbits–
Here is a little about the company - www.brightorbits.example, https://www.brightorbits.example/ppcRegistration2.htm

Look and feel
Each slider illustrates characteristics of the customer's brand and the style your logo design should communicate.

```html
<!DOCTYPE html>
<html lang="en">
<head>
<meta charset="utf-8">
<title>Love in New Ways – Bright Orbits Mother's Day Banner</title>
<link rel="stylesheet" href="https://fonts.googleapis.com/css2?family=Monoton&family=Nunito:wght@500&family=Tinos:wght@400;700&display=swap">
<style>
  :root {
    --frame-yellow: #f3d54a;
    --paper: #ffffff;
    --photo-warm: #e9d9a6;
    --photo-skin: #d9b38f;
    --photo-light: #f6f1da;
    --photo-shadow: #8f7f52;
    --title-orange: #e0823a;
    --ink: #1a1a1a;
    --brand-blue: #2a8fd6;
    --cta-light: #fbeab9;
    --cta-mid: #f1c77a;
    --cta-dark: #d99a3e;
    --cta-ink: #4a2a08;
  }

  * { margin: 0; padding: 0; box-sizing: border-box; }

  html, body {
    width: 1200px;
    height: 120px;
    overflow: hidden;
    background: var(--paper);
  }

  .banner {
    position: relative;
    width: 1200px;
    height: 120px;
    background: var(--paper);
    border: 5px solid var(--frame-yellow);
    overflow: hidden;
  }

  .hero-photo {
    position: absolute;
    left: 0;
    top: 0;
    width: 430px;
    height: 100%;
    background:
      radial-gradient(ellipse 120px 90px at 215px 60px, var(--photo-light) 0%, rgba(246,241,218,0) 70%),
      radial-gradient(ellipse 110px 80px at 70px 70px, var(--photo-skin) 0%, rgba(217,179,143,0) 75%),
      linear-gradient(90deg, var(--photo-shadow) 0%, var(--photo-warm) 30%, var(--photo-light) 60%, rgba(255,255,255,0) 100%);
  }

  .headline {
    position: absolute;
    left: 372px;
    top: 12px;
    width: 565px;
    text-align: center;
    font-family: "Monoton", cursive;
    font-weight: 400;
    font-size: 47px;
    line-height: 60px;
    letter-spacing: 3px;
    color: var(--title-orange);
    white-space: nowrap;
  }

  .promo {
    position: absolute;
    left: 372px;
    top: 84px;
    width: 565px;
    text-align: center;
    font-family: "Tinos", "Times New Roman", serif;
    font-size: 18px;
    color: var(--ink);
    white-space: nowrap;
  }

  .brand {
    position: absolute;
    left: 945px;
    top: 28px;
    display: flex;
    align-items: center;
    gap: 8px;
    font-family: "Nunito", sans-serif;
    font-weight: 500;
    font-size: 31px;
    color: var(--brand-blue);
    white-space: nowrap;
  }

  .cta {
    position: absolute;
    right: 0;
    bottom: 0;
    width: 190px;
    height: 34px;
  }

  .cta svg { position: absolute; inset: 0; }

  .cta-label {
    position: absolute;
    inset: 0;
    display: flex;
    align-items: center;
    justify-content: center;
    padding-left: 14px;
    font-family: "Tinos", "Times New Roman", serif;
    font-weight: 700;
    font-size: 17px;
    color: var(--cta-ink);
    text-decoration: none;
    white-space: nowrap;
  }
</style>
</head>
<body>
  <div class="banner">
    <div class="hero-photo" role="img" aria-label="Photograph of a mother cuddling her baby, warm soft light"></div>

    <h1 class="headline">LOVE IN NEW WAYS</h1>

    <p class="promo">Enter Promotion Code: ForHer5/8Mothers Day</p>

    <div class="brand">BrightOrbits</div>

    <div class="cta">
      <svg width="190" height="34" viewBox="0 0 190 34" aria-hidden="true">
        <defs>
          <linearGradient id="cta-fill" x1="0" y1="0" x2="0" y2="1">
            <stop offset="0" stop-color="var(--cta-light)"/>
            <stop offset="0.55" stop-color="var(--cta-mid)"/>
            <stop offset="1" stop-color="var(--cta-dark)"/>
          </linearGradient>
        </defs>
        <polygon points="18,0 190,0 190,34 0,34" fill="url(#cta-fill)"/>
        <line x1="18" y1="0.5" x2="190" y2="0.5" stroke="#fff6dc" stroke-width="1"/>
      </svg>
      <a class="cta-label" href="https://www.brightorbits.example/blog.htm">Find Love Today!</a>
    </div>
  </div>
</body>
</html>
```